FotoVELTA buisnesscard

Hey :) I need a modern buisnesscard for my company FotoVELTA
It most have:
Dagligleder og Fotograf: Henrik Torvald Bjelland

Mob: +4791642058
Epost: post@fotovelta.no
Adresse: Bakkestien22, 6095 Nordvik

Facbook and instagram logo with text FotoVELTA

FotoVELTA logo

It Company

```html
<!DOCTYPE html>
<html lang="no">
<head>
<meta charset="utf-8">
<title>FotoVELTA – visittkort</title>
<link href="https://fonts.googleapis.com/css2?family=Exo+2:wght@600;700&family=Roboto:wght@400&display=swap" rel="stylesheet">
<style>
  :root {
    --page-bg: #2a2422;
    --card-bg: #121212;
    --card-edge: #1d1d1d;
    --mark-tone: #191919;
    --text-white: #f2f2f2;
    --text-silver: #d0d0d0;
    --text-grey: #a7a7a7;
    --icon-grey: #9a9a9a;
  }
  * { margin: 0; padding: 0; box-sizing: border-box; }
  html, body {
    width: 1200px; height: 900px; overflow: hidden;
    background: var(--page-bg);
  }
  .sheet {
    position: relative; width: 1200px; height: 900px;
    display: flex; align-items: center; justify-content: center; gap: 40px;
  }
  .card {
    position: relative; width: 540px; height: 318px;
    background: var(--card-bg);
    border: 1px solid var(--card-edge);
    border-radius: 4px;
    overflow: hidden;
    box-shadow: 0 18px 40px rgba(0,0,0,.45);
  }
  .faint-mark {
    position: absolute;
    background: var(--mark-tone);
    border-radius: 22px;
  }
  .card--front .faint-mark { left: 290px; top: 30px; width: 240px; height: 260px; }
  .card--back .faint-mark { left: 250px; top: -30px; width: 320px; height: 320px; }

  .brand-name {
    position: absolute;
    font-family: "Exo 2", sans-serif; font-weight: 700;
    color: var(--text-white);
    letter-spacing: .3px;
    white-space: nowrap;
  }
  .card--front .brand-name { left: 305px; top: 128px; font-size: 34px; line-height: 40px; }
  .card--back .brand-name { left: 0; right: 0; top: 130px; text-align: center; font-size: 50px; line-height: 58px; color: var(--text-silver); }

  .holder { position: absolute; left: 30px; top: 126px; }
  .holder-name {
    font-family: "Exo 2", sans-serif; font-weight: 700;
    font-size: 15px; line-height: 18px; color: var(--text-white); text-transform: uppercase; letter-spacing: .3px;
  }
  .holder-role {
    margin-top: 3px;
    font-family: "Roboto", sans-serif; font-size: 11px; line-height: 14px; color: var(--text-grey);
  }

  .social {
    position: absolute; right: 24px; top: 214px;
    display: flex; align-items: center; gap: 7px;
    font-family: "Roboto", sans-serif; font-size: 11px; line-height: 14px; color: var(--text-grey);
  }
  .social-square { width: 10px; height: 10px; background: var(--icon-grey); border-radius: 2px; }

  .contact { position: absolute; left: 30px; bottom: 26px; list-style: none; }
  .contact li {
    display: flex; align-items: center; gap: 8px;
    font-family: "Roboto", sans-serif; font-size: 11px; color: var(--text-white);
    line-height: 17px;
  }
  .contact svg { width: 10px; height: 10px; fill: var(--icon-grey); flex: none; }
</style>
</head>
<body>
<main class="sheet">
  <section class="card card--front" aria-label="Visittkort forside">
    <div class="faint-mark"></div>
    <div class="holder">
      <p class="holder-name">Henrik Torvald Bjelland</p>
      <p class="holder-role">Dagligleder og Fotograf</p>
    </div>
    <div class="brand-name">FotoVELTA</div>
    <div class="social"><span class="social-square"></span><span>FotoVELTA</span></div>
    <ul class="contact">
      <li>
        <svg viewBox="0 0 10 10"><rect x="2.5" y="0.5" width="5" height="9" rx="1"/><rect x="3.5" y="1.8" width="3" height="5.5" fill="#121212"/></svg>
        +4791642058
      </li>
      <li>
        <svg viewBox="0 0 10 10"><rect x="0.5" y="2" width="9" height="6.5" rx="0.8"/><path d="M1 2.5 L5 5.8 L9 2.5" stroke="#121212" stroke-width="1" fill="none"/></svg>
        post@fotovelta.no
      </li>
      <li>
        <svg viewBox="0 0 10 10"><path d="M5 0.5a3.3 3.3 0 0 1 3.3 3.3C8.3 6.2 5 9.5 5 9.5S1.7 6.2 1.7 3.8A3.3 3.3 0 0 1 5 0.5z"/><circle cx="5" cy="3.8" r="1.2" fill="#121212"/></svg>
        Bakkestien22, 6095 Nordvik
      </li>
    </ul>
  </section>

  <section class="card card--back" aria-label="Visittkort bakside">
    <div class="faint-mark"></div>
    <div class="brand-name">FotoVELTA</div>
  </section>
</main>
</body>
</html>
```